Oakhaven Construction Need an information and interactive website with client portal. We have ou

Need to have a client log in screen for work orders and estimate requests.
Nice informational landing page.

Oakhaven is a full service general contractor servicing apartment complexes;
maintenance of grounds and apartments - remodeling and construction.

Design Specifics: We are pretty open here. Some good examples are
www.marrowpeakbuilders.com , tovelresidence.com and www.quillbyworksite.com

For the site we need:
Homepage - to explain services
Roofing page
Apartment Page
Client Portal - where clients can set up accounts to set up work/estimate request that will be routed to our email

--Will need coding, plan to host site on Wordpress

Target Market(s)

Multi family, Residential and commercial clients

Industry/Entity Type

Construction

Coding

Coded - Design and coding required

Number of Pages Required

3 page

Font styles to use
Serif

Requirements
Must have
• Client portal
Nice to have
• Not sure. please advise

```html
<!DOCTYPE html>
<html lang="en">
<head>
<meta charset="utf-8">
<title>Oakhaven Construction</title>
<link href="https://fonts.googleapis.com/css2?family=Source+Sans+3:wght@400;600;700;800&display=swap" rel="stylesheet">
<style>
:root{
  --red:#b5141b;
  --yellow:#fbbb22;
  --blue:#0c1a93;
  --black:#151515;
  --charcoal:#333333;
  --grey-bg:#ebebeb;
  --text:#444444;
  --white:#ffffff;
  --font:"Source Sans 3",Arial,sans-serif;
}
*{box-sizing:border-box;margin:0;padding:0}
html,body{width:1200px;height:3203px;overflow:hidden;background:var(--white);font-family:var(--font);color:var(--text)}
.page{position:relative;width:1200px;height:3203px;overflow:hidden}
.abs{position:absolute}

/* top strip */
.topbar{left:0;top:0;width:1200px;height:30px;background:var(--black)}
.topbar .auth{left:775px;top:8px;color:var(--white);font-size:11px;font-weight:700;letter-spacing:.5px}
.topbar .auth span{margin:0 6px;opacity:.6}
.social{left:866px;top:6px;display:flex;gap:5px}
.social i{display:block;width:17px;height:17px;border-radius:50%}

/* header */
.header{left:0;top:30px;width:1200px;height:70px;background:var(--white)}
.brand{display:flex;align-items:center;justify-content:center;gap:8px;background:var(--white);box-shadow:0 1px 3px rgba(0,0,0,.15);white-space:nowrap}
.brand b{display:block;width:16px;height:16px;background:var(--red);flex:none}
.brand span{font-size:22px;font-weight:800;color:var(--red);letter-spacing:.5px}
.header .brand{left:232px;top:6px;width:166px;height:52px}
.contact{top:24px;font-size:8px;line-height:11px;color:#555}
.contact strong{color:var(--black);margin-right:8px}

/* nav */
.nav{left:230px;top:94px;width:735px;height:41px;background:var(--red);display:flex;align-items:center;z-index:3}
.nav a{display:block;height:41px;line-height:41px;padding:0 28px;color:var(--white);font-size:11px;font-weight:700;text-decoration:none}
.nav a.active{background:var(--yellow);color:var(--black);height:45px;margin-top:-4px;line-height:49px;padding:0 32px}
.nav .search{margin-left:auto;margin-right:18px;width:120px;height:20px;background:var(--white);font-size:8px;color:#999;padding:4px 6px;position:relative}
.nav .search svg{position:absolute;right:5px;top:5px}

/* hero */
.hero{left:0;top:112px;width:1200px;height:475px;background:linear-gradient(180deg,#77756c 0%,#55574d 40%,#3b4432 75%,#2a3322 100%)}
.hero h1{left:248px;top:135px;color:var(--white);font-size:42px;line-height:40px;font-weight:700;letter-spacing:.5px}
.hero p{left:248px;top:222px;color:var(--white);font-size:15px;line-height:19px}
.btn{display:block;text-align:center;font-size:9px;font-weight:700;letter-spacing:.3px}
.hero .btn-yellow{left:250px;top:300px;width:145px;height:38px;line-height:38px;background:var(--yellow);color:var(--white)}
.hero .btn-outline{left:407px;top:300px;width:143px;height:38px;line-height:36px;border:2px solid var(--white);color:var(--white)}
.dots{left:562px;top:433px;display:flex;gap:12px}
.dots i{width:10px;height:10px;border-radius:50%;background:var(--white)}
.dots i:first-child{background:var(--red)}

.login{left:758px;top:106px;width:207px;height:234px;background:var(--white);border:5px solid #e6e6e6;text-align:center;padding-top:16px}
.login .pre{font-size:8px;color:#777}
.login .title{font-size:13px;font-weight:800;color:var(--red)}
.login .field{margin:8px auto 0;width:140px;height:20px;background:#ececec;font-size:7px;color:#888;text-align:left;padding:5px 0 0 26px}
.login .go{margin:12px auto 0;width:140px;height:20px;line-height:20px;background:var(--yellow);color:var(--white);font-size:7px;font-weight:700}
.login .ask{margin-top:18px;font-size:7px;color:#666}
.login .up{margin:6px auto 0;width:140px;height:20px;line-height:20px;background:var(--red);color:var(--white);font-size:7px;font-weight:700}

/* welcome */
.welcome-title{left:0;top:642px;width:1200px;text-align:center;font-size:28px;font-weight:600;color:var(--charcoal)}
.welcome-title em{font-style:normal;color:var(--red)}
.rule{left:570px;top:688px;width:60px;height:2px;background:#c9c9c9}
.welcome-text{left:235px;top:703px;width:730px;font-size:9px;line-height:14px;text-align:justify;color:#666}
.strip{left:235px;top:803px;width:730px;height:158px;display:flex}
.strip div{flex:1}

/* services */
.service{left:0;width:1200px;height:374px}
.service .half{position:absolute;top:0;width:600px;height:374px}
.service h3{position:absolute;color:var(--white);font-size:18px;line-height:21px;font-weight:700}
.service .icon{position:absolute;width:78px;height:78px;border:2px solid var(--white);padding:5px}
.service .icon div{width:100%;height:100%;background:var(--white);display:flex;align-items:center;justify-content:center}
.service p{position:absolute;color:var(--white);font-size:9px;line-height:16px}
.service .more{position:absolute;width:98px;height:34px;line-height:34px;background:var(--white);font-size:9px;font-weight:700;text-align:center}

/* projects */
.section-title{left:0;width:1200px;text-align:center;font-size:28px;font-weight:600;color:var(--black)}
.arrow{font-size:34px;color:#555;font-weight:400}
.project{width:166px;height:222px}
.project.raised{box-shadow:0 6px 10px rgba(0,0,0,.3)}
.label{width:166px;text-align:center;font-size:13px;font-weight:700;color:var(--charcoal)}

/* news */
.news{left:0;top:2573px;width:1200px;height:352px;background:var(--grey-bg)}
.news-card{top:124px;width:166px;height:164px;background:var(--white)}
.news-card .photo{height:124px}
.news-card .cap{padding:6px 8px;font-size:7px;line-height:10px}
.news-card .cap b{display:block;color:var(--black)}
.news-card.hot .cap{background:var(--red);color:var(--white)}
.news-card.hot .cap b{color:var(--white)}

/* partners */
.partners{left:0;top:2925px;width:1200px;height:213px;background:var(--charcoal)}
.partners h2{top:52px;color:var(--white)}
.partners .arrow{color:var(--white)}
.badge{top:138px;height:40px;border:2px solid #cfcfcf;opacity:.85}

/* footer */
.footer{left:0;top:3138px;width:1200px;height:65px;background:var(--red)}
.footer .brand{left:265px;top:14px;width:94px;height:38px;gap:5px}
.footer .brand span{font-size:13px;letter-spacing:.2px}
.footer .brand b{width:10px;height:10px}
.footer nav{left:384px;top:26px;font-size:9px;font-weight:700;color:var(--white)}
.footer nav span{margin:0 9px}
.footer .copy{left:836px;top:26px;font-size:9px;color:var(--white)}
</style>
</head>
<body>
<div class="page">

  <div class="abs topbar">
    <div class="abs auth">LOGIN<span>|</span>SIGNUP</div>
    <div class="abs social"><i style="background:#3b5bbb"></i><i style="background:#2aa3e8"></i><i style="background:#c8327a"></i><i style="background:#cf2027"></i></div>
  </div>

  <header class="abs header">
    <div class="abs brand"><b></b><span>OAKHAVEN</span></div>
    <div class="abs contact" style="left:590px"><strong>Address:</strong>1840 Alder Ridge Road, Suite 12<br>Westfield Park, TX 75001</div>
    <div class="abs contact" style="left:805px"><strong>Tel.:</strong>+1 555 014 2290<br><strong>Email:</strong>hello@oakhavenbuild.com</div>
  </header>

  <nav class="abs nav">
    <a class="active" href="#">HOME</a><a href="#">ROOFING</a><a href="#">APARTMENT</a><a href="#">CLIENT PORTAL</a>
    <div class="search">Search Here
      <svg width="10" height="10" viewBox="0 0 10 10"><circle cx="4" cy="4" r="3" fill="none" stroke="#333" stroke-width="1.4"/><line x1="6.3" y1="6.3" x2="9.3" y2="9.3" stroke="#333" stroke-width="1.6"/></svg>
    </div>
  </nav>

  <section class="abs hero" role="img" aria-label="City skyline with office towers and trees at dusk">
    <h1 class="abs">BUILD YOUR DREAM<br>BUILD IT RIGHT</h1>
    <p class="abs">Lorem ipsum dolor sit amet, consectetuer adipiscing elit.<br>Aenean commodo ligula eget dolor.</p>
    <a class="abs btn btn-yellow">VIEW OUR SERVICES</a>
    <a class="abs btn btn-outline">GET IN TOUCH</a>
    <div class="abs dots"><i></i><i></i><i></i><i></i></div>
    <form class="abs login">
      <div class="pre">LOG IN TO</div>
      <div class="title">OAKHAVEN</div>
      <div class="field">Username</div>
      <div class="field">••••••••••</div>
      <div class="go">LOGIN</div>
      <div class="ask">Don't have an Account?</div>
      <div class="up">SIGN UP</div>
    </form>
  </section>

  <h2 class="abs welcome-title">WELCOME TO <em>OAKHAVEN</em> CONSTRUCTION</h2>
  <div class="abs rule"></div>
  <p class="abs welcome-text">Lorem ipsum dolor sit amet, consectetuer adipiscing elit. Aenean commodo ligula eget dolor. Aenean massa. Cum sociis natoque penatibus et magnis dis parturient montes, nascetur ridiculus mus. Donec quam felis, ultricies nec, pellentesque eu, pretium quis, sem. Nulla consequat massa quis enim. Donec pede justo, fringilla vel, aliquet nec, vulputate eget, arcu. In enim justo, rhoncus ut, imperdiet a, venenatis vitae, justo. Nullam dictum felis eu pede mollis pretium. Integer tincidunt. Cras dapibus. Vivamus elementum semper nisi. Aenean vulputate eleifend tellus. Aenean leo ligula, porttitor eu, consequat vitae, eleifend ac, enim. Aliquam lorem ante, dapibus in, viverra quis, feugiat a, tellus.</p>
  <div class="abs strip">
    <div role="img" aria-label="Workers silhouetted on a rooftop at sunset" style="background:linear-gradient(180deg,#e4d8bf 0%,#b7a27c 45%,#2b241b 100%)"></div>
    <div role="img" aria-label="Tower crane against the sky in black and white" style="background:linear-gradient(200deg,#e2e4e5 0%,#a6aaad 55%,#4f5357 100%)"></div>
    <div role="img" aria-label="Engineer in hard hat reviewing plans on a site" style="flex:2.3;background:linear-gradient(100deg,#8fb3d8 0%,#c7d8ea 45%,#eef2f6 100%)"></div>
  </div>

  <section class="abs service" style="top:1020px">
    <div class="half" style="left:0;background:var(--red)">
      <h3 style="right:120px;top:37px;text-align:right">FULL SERVICE GENERAL<br>CONTRACTOR SERVICING<br>APARTMENT COMPLEXES</h3>
      <div class="icon" style="left:494px;top:30px"><div><svg width="40" height="40" viewBox="0 0 40 40"><circle cx="18" cy="22" r="9" fill="var(--red)"/><path d="M8 16a10 10 0 0 1 20 0z" fill="var(--red)"/><circle cx="31" cy="30" r="5" fill="none" stroke="var(--red)" stroke-width="3"/></svg></div></div>
      <p style="left:224px;top:124px;width:348px;text-align:right">Lorem ipsum dolor sit amet, consectetuer adipiscing elit. Aenean commodo ligula eget dolor. Aenean massa. Cum sociis natoque penatibus et magnis dis parturient montes, nascetur ridiculus mus. Donec quam felis, ultricies nec, pellentesque eu, pretium quis, sem. Nulla consequat massa quis enim. Donec pede justo, fringilla vel, aliquet nec, vulputate eget, arcu. In enim justo, rhoncus ut, imperdiet a, venenatis vitae, justo. Nullam dictum felis eu pede mollis pretium. Integer tincidunt. Cras dapibus. Vivamus elementum semper nisi. Aenean vulputate eleifend tellus. Aenean leo ligula, porttitor eu, consequat vitae, eleifend ac, enim. Aliquam lorem ante, dapibus in, viverra quis, feugiat a, tellus.</p>
      <a class="more" style="left:468px;top:291px;color:var(--red)">LEARN MORE</a>
    </div>
    <div class="half" style="left:600px;background:linear-gradient(165deg,#d9d2df 0%,#9c9fc4 30%,#5568a8 60%,#2a3a78 100%)" role="img" aria-label="Glass skyscrapers seen from below against a cloudy blue sky"></div>
  </section>

  <section class="abs service" style="top:1394px">
    <div class="half" style="left:0;background:linear-gradient(180deg,#c3cbc9 0%,#cdb48a 38%,#b88a52 65%,#7d5530 100%)" role="img" aria-label="Yellow excavator digging a mound of soil"></div>
    <div class="half" style="left:600px;background:var(--yellow)">
      <div class="icon" style="left:23px;top:30px"><div><svg width="40" height="40" viewBox="0 0 40 40"><circle cx="14" cy="10" r="5" fill="var(--yellow)"/><path d="M8 18h12l4 12h-6l-2-6-4 14H6z" fill="var(--yellow)"/><rect x="24" y="30" width="12" height="6" fill="var(--yellow)"/></svg></div></div>
      <h3 style="left:122px;top:37px">MAINTENANCE OF<br>GROUNDS AND<br>APARTMENTS</h3>
      <p style="left:23px;top:124px;width:350px">Lorem ipsum dolor sit amet, consectetuer adipiscing elit. Aenean commodo ligula eget dolor. Aenean massa. Cum sociis natoque penatibus et magnis dis parturient montes, nascetur ridiculus mus. Donec quam felis, ultricies nec, pellentesque eu, pretium quis, sem. Nulla consequat massa quis enim. Donec pede justo, fringilla vel, aliquet nec, vulputate eget, arcu. In enim justo, rhoncus ut, imperdiet a, venenatis vitae, justo. Nullam dictum felis eu pede mollis pretium. Integer tincidunt. Cras dapibus. Vivamus elementum semper nisi. Aenean vulputate eleifend tellus. Aenean leo ligula, porttitor eu, consequat vitae, eleifend ac, enim. Aliquam lorem ante, dapibus in, viverra quis, feugiat a, tellus.</p>
      <a class="more" style="left:30px;top:293px;color:var(--yellow)">LEARN MORE</a>
    </div>
  </section>

  <section class="abs service" style="top:1768px">
    <div class="half" style="left:0;background:var(--blue)">
      <h3 style="right:120px;top:50px;text-align:right">REMODELING AND<br>CONSTRUCTION</h3>
      <div class="icon" style="left:494px;top:30px"><div><svg width="40" height="40" viewBox="0 0 40 40"><path d="M6 36L20 6l14 30z" fill="none" stroke="var(--blue)" stroke-width="3"/><rect x="17" y="20" width="6" height="16" fill="var(--blue)"/></svg></div></div>
      <p style="left:224px;top:124px;width:348px;text-align:right">Lorem ipsum dolor sit amet, consectetuer adipiscing elit. Aenean commodo ligula eget dolor. Aenean massa. Cum sociis natoque penatibus et magnis dis parturient montes, nascetur ridiculus mus. Donec quam felis, ultricies nec, pellentesque eu, pretium quis, sem. Nulla consequat massa quis enim. Donec pede justo, fringilla vel, aliquet nec, vulputate eget, arcu. In enim justo, rhoncus ut, imperdiet a, venenatis vitae, justo. Nullam dictum felis eu pede mollis pretium. Integer tincidunt. Cras dapibus. Vivamus elementum semper nisi. Aenean vulputate eleifend tellus. Aenean leo ligula, porttitor eu, consequat vitae, eleifend ac, enim. Aliquam lorem ante, dapibus in, viverra quis, feugiat a, tellus.</p>
      <a class="more" style="left:468px;top:291px;color:var(--blue)">LEARN MORE</a>
    </div>
    <div class="half" style="left:600px;background:linear-gradient(200deg,#4f88cc 0%,#8fb6de 40%,#cfdde6 70%,#eedca0 100%)" role="img" aria-label="Yellow tower cranes against a bright blue sky"></div>
  </section>

  <h2 class="abs section-title" style="top:2178px">LATEST PROJECTS</h2>
  <div class="abs arrow" style="left:192px;top:2343px">&#10094;</div>
  <div class="abs arrow" style="left:982px;top:2343px">&#10095;</div>
  <div class="abs project" style="left:235px;top:2259px;background:linear-gradient(180deg,#4f86cf 0%,#8fb0d6 55%,#9aa6b0 100%)" role="img" aria-label="Historic domed tower building under blue sky"></div>
  <div class="abs project raised" style="left:423px;top:2246px;background:linear-gradient(160deg,#e0e1e2 0%,#a99384 45%,#5a4234 100%)" role="img" aria-label="Angular brick high-rise seen from below"></div>
  <div class="abs project" style="left:611px;top:2259px;background:linear-gradient(180deg,#84afdc 0%,#c1d3e2 55%,#d3d3cf 100%)" role="img" aria-label="Pyramid skyscraper above a city"></div>
  <div class="abs project" style="left:798px;top:2259px;background:linear-gradient(180deg,#163f8c 0%,#3a72bf 55%,#8ab3dd 100%)" role="img" aria-label="Glass tower reaching into deep blue sky"></div>
  <div class="abs label" style="left:235px;top:2489px">LOREM IPSUM</div>
  <div class="abs label" style="left:423px;top:2476px">LOREM IPSUM</div>
  <div class="abs label" style="left:611px;top:2489px">LOREM IPSUM</div>
  <div class="abs label" style="left:798px;top:2489px">LOREM IPSUM</div>

  <section class="abs news">
    <h2 class="abs section-title" style="top:55px">LATEST NEWS</h2>
    <article class="abs news-card" style="left:235px"><div class="photo" role="img" aria-label="Construction worker in safety vest on a site" style="background:linear-gradient(180deg,#d3d5d1 0%,#aeb0a6 55%,#7f8277 100%)"></div><div class="cap"><b>LOREM IPSUM</b>JUNE 18, 2016</div></article>
    <article class="abs news-card hot" style="left:423px"><div class="photo" role="img" aria-label="Tower crane silhouetted against a red sky" style="background:linear-gradient(180deg,#ead0c8 0%,#cf7d70 55%,#a8352d 100%)"></div><div class="cap"><b>LOREM IPSUM</b>JUNE 18, 2016</div></article>
    <article class="abs news-card" style="left:611px"><div class="photo" role="img" aria-label="Tall tower against a blue sky" style="background:linear-gradient(180deg,#2458ad 0%,#5c91d3 55%,#a8c8e8 100%)"></div><div class="cap"><b>LOREM IPSUM</b>JUNE 18, 2016</div></article>
    <article class="abs news-card" style="left:798px"><div class="photo" role="img" aria-label="Gloved hand holding a tool on wood" style="background:linear-gradient(135deg,#d92b2a 0%,#c9634a 45%,#b9996f 100%)"></div><div class="cap"><b>LOREM IPSUM</b>JUNE 18, 2016</div></article>
  </section>

  <section class="abs partners">
    <h2 class="abs section-title">OUR PARTNERS</h2>
    <div class="abs arrow" style="left:192px;top:130px">&#10094;</div>
    <div class="abs arrow" style="left:982px;top:130px">&#10095;</div>
    <div class="abs badge" style="left:262px;width:40px;border-radius:50%"></div>
    <div class="abs badge" style="left:450px;width:110px"></div>
    <div class="abs badge" style="left:632px;width:120px"></div>
    <div class="abs badge" style="left:842px;width:40px;border-radius:50%"></div>
  </section>

  <footer class="abs footer">
    <div class="abs brand"><b></b><span>OAKHAVEN</span></div>
    <nav class="abs">HOME<span>|</span>ROOFING<span>|</span>APPARTMENT<span>|</span>CLIENT PORTAL</nav>
    <div class="abs copy">Copyright © 2016 Oakhaven</div>
  </footer>

</div>
</body>
</html>
```